Irrigation Business needs their business cards modernised and revamped

I would like to keep my current logo, colours and revamp the format of the card.

I would like the card to be clean yet important.

Im not sure if you include texture but i would like the named logo to be indented into the card etc.

show me something alive and free something thats clinical to the point yet has a feel of achievement. i would like people to go nice card.

Target Market(s)

high end clients, corporate, sports field manger, the guys that make the decisions

Industry/Entity Type

Business

Contact Information for Business Card

nformation to be included

Gareth Minchin (Director)
0472958316
gareth@tkwater.biz
www.tomskerrywatering.com

instagram logo
google logo
facebook logo

Colors

Designer to choose colors to be used in the design.

Requirements
Nice to have
• indentations a really nice feel to the card good texture

```html
<!DOCTYPE html>
<html lang="en">
<head>
<meta charset="utf-8">
<title>Tom's Kerry Watering – Business Cards</title>
<link href="https://fonts.googleapis.com/css2?family=Montserrat:wght@400;600;700&display=swap" rel="stylesheet">
<style>
  :root {
    --brand-blue: #2f67ad;
    --deep-blue: #2b5da6;
    --sky-blue: #29a3d8;
    --ink-grey: #6f6f6f;
    --paper: #ffffff;
    --stage: #e9ebee;
    --faint: #f1f1f1;
  }
  * { margin: 0; padding: 0; box-sizing: border-box; }
  html, body { width: 1200px; height: 810px; overflow: hidden; }
  body {
    background: var(--stage);
    font-family: "Montserrat", sans-serif;
    position: relative;
  }
  .card {
    position: absolute;
    top: 250px;
    width: 540px;
    height: 310px;
    overflow: hidden;
    box-shadow: 0 6px 18px rgba(0,0,0,.18);
  }
  /* Back face */
  .card--back { left: 40px; background: var(--brand-blue); }
  .card__map {
    position: absolute;
    left: 70px; top: 40px; width: 400px; height: 230px;
    background: radial-gradient(ellipse at center, rgba(255,255,255,.09), rgba(255,255,255,0) 70%);
  }
  .back-logo {
    position: absolute;
    left: 0; right: 0; top: 92px;
    display: flex; flex-direction: column; align-items: center; gap: 14px;
  }
  .back-logo__dot {
    width: 64px; height: 64px; border-radius: 50%;
    border: 3px solid var(--paper);
  }
  .back-logo__name {
    color: var(--paper);
    font-weight: 700;
    font-size: 25px;
    letter-spacing: .5px;
    text-transform: uppercase;
  }
  .socials {
    position: absolute; left: 0; right: 0; top: 232px;
    display: flex; justify-content: center; gap: 6px;
  }
  .socials__dot { width: 12px; height: 12px; border-radius: 50%; background: var(--paper); }

  /* Front face */
  .card--front { left: 620px; background: var(--paper); }
  .card__mark-area {
    position: absolute;
    left: -70px; top: 20px; width: 270px; height: 270px; border-radius: 50%;
    background: radial-gradient(circle, var(--faint) 0%, #f6f6f6 60%, rgba(255,255,255,0) 72%);
  }
  .front-logo {
    position: absolute; right: 28px; top: 30px;
    display: flex; flex-direction: column; align-items: center; gap: 8px;
  }
  .front-logo__dot {
    width: 52px; height: 52px; border-radius: 50%;
    background: var(--sky-blue);
  }
  .front-logo__name {
    color: var(--deep-blue);
    font-weight: 700;
    font-size: 17px;
    text-transform: uppercase;
  }
  .website {
    position: absolute; right: 28px; top: 150px;
    color: var(--ink-grey); font-size: 12.5px;
  }
  .holder {
    position: absolute; left: 60px; top: 222px;
  }
  .holder__name { color: var(--deep-blue); font-weight: 600; font-size: 21px; }
  .holder__role { color: var(--ink-grey); font-size: 15px; }
  .contact {
    position: absolute; left: 268px; top: 196px;
    color: var(--ink-grey); font-size: 13.5px; line-height: 1.55;
  }
  .band { position: absolute; bottom: 0; height: 9px; }
  .band--sky { left: 0; width: 68%; background: var(--sky-blue); }
  .band--deep { left: 69.5%; right: 0; background: var(--deep-blue); height: 12px; }
</style>
</head>
<body>
  <section class="card card--back">
    <div class="card__map" role="img" aria-label="Faint dotted world map"></div>
    <div class="back-logo">
      <span class="back-logo__dot"></span>
      <span class="back-logo__name">Tom's Kerry Watering</span>
    </div>
    <div class="socials" aria-label="Social links">
      <span class="socials__dot"></span>
      <span class="socials__dot"></span>
      <span class="socials__dot"></span>
    </div>
  </section>

  <section class="card card--front">
    <div class="card__mark-area" role="img" aria-label="Large faint brand emblem decoration"></div>
    <div class="front-logo">
      <span class="front-logo__dot"></span>
      <span class="front-logo__name">Tom's Kerry Watering</span>
    </div>
    <p class="website">www.tomskerrywatering.com</p>
    <div class="holder">
      <p class="holder__name">Gareth Minchin</p>
      <p class="holder__role">Director</p>
    </div>
    <div class="contact">
      <p>0472958316</p>
      <p>gareth@tkwater.biz</p>
    </div>
    <span class="band band--sky"></span>
    <span class="band band--deep"></span>
  </section>
</body>
</html>
```